Business Card Design Project

I need a business card design for our new logo, please check the logo at the following link:
https://www.filecrate.net/s/q7rtx2pw9kd41m/FernLoop.png
The address on the business card:
Av. Gervásio Tavares 418 sala 207
Barra da Tijuca, Rio de Janeiro, RJ
CEP: 22714-380
Brasil
Phone: +55 21 86347215
e-mail: osvaldo@fernloop.com.br
Updates
Thank you all for sending your designs, we will not provide feedback because there are too many designs, on December 3 we will pick the best design according to our point of view. Please keep posting.
Osvaldo
Industry/Entity Type
Business
Look and feel
Each slider illustrates characteristics of the customer's brand and the style your logo design should communicate.

```html
<!DOCTYPE html>
<html lang="en">
<head>
<meta charset="utf-8">
<title>FernLoop Business Card</title>
<link rel="stylesheet" href="https://fonts.googleapis.com/css2?family=Exo+2:wght@400;600;700&display=swap">
<style>
  :root {
    --backdrop: #e9e9e9;
    --card-white: #ffffff;
    --brand-yellow: #f7cf12;
    --ink: #231f20;
    --figure-dark: #2a2626;
    --figure-gold: #d4b01a;
  }
  * { box-sizing: border-box; margin: 0; padding: 0; }
  html, body {
    width: 1200px; height: 1000px; overflow: hidden;
    background: var(--backdrop);
    font-family: "Exo 2", sans-serif;
    color: var(--ink);
  }
  .stage { position: relative; width: 1200px; height: 1000px; }
  .card {
    position: absolute; top: 335px;
    width: 527px; height: 330px;
    box-shadow: 0 3px 8px rgba(0,0,0,0.25);
  }
  .card--front { left: 45px; background: var(--card-white); }
  .card--back { left: 628px; background: var(--brand-yellow); }

  .front__wordmark {
    position: absolute; left: 0; right: 0; top: 62px;
    text-align: center;
    font-size: 92px; font-weight: 700; letter-spacing: -1px;
    line-height: 1;
  }
  .front__figures {
    position: absolute; left: 48px; right: 48px; top: 190px;
    display: flex; justify-content: space-between;
  }
  .figure-slot {
    width: 100px; height: 72px; border-radius: 6px;
    background: linear-gradient(135deg, var(--figure-gold) 0%, var(--figure-dark) 60%);
  }

  .back__identity { position: absolute; left: 37px; top: 78px; }
  .identity__name { font-size: 30px; font-weight: 700; line-height: 1.1; }
  .identity__position { font-size: 18px; font-weight: 700; margin-top: 2px; }

  .back__contacts {
    position: absolute; left: 37px; top: 150px;
    list-style: none; font-size: 12.5px; line-height: 1.35;
  }
  .contact { display: flex; align-items: flex-start; margin-bottom: 10px; }
  .contact__icon { width: 12px; height: 12px; margin: 2px 12px 0 0; flex: none; fill: var(--ink); }

  .back__brand {
    position: absolute; right: 40px; top: 72px; width: 190px;
    text-align: center;
  }
  .brand__figure {
    width: 170px; height: 115px; margin: 0 auto; border-radius: 8px;
    background: linear-gradient(135deg, #ffffff 0%, var(--figure-dark) 45%);
  }
  .brand__name { font-size: 44px; font-weight: 700; line-height: 1; margin-top: 10px; }
</style>
</head>
<body>
<main class="stage">
  <section class="card card--front">
    <div class="front__wordmark">FernLoop</div>
    <div class="front__figures">
      <div class="figure-slot" role="img" aria-label="Brand mascot illustration running with a briefcase"></div>
      <div class="figure-slot" role="img" aria-label="Brand mascot illustration running with a briefcase"></div>
      <div class="figure-slot" role="img" aria-label="Brand mascot illustration running with a briefcase"></div>
    </div>
  </section>

  <section class="card card--back">
    <div class="back__identity">
      <h1 class="identity__name">Name Surname</h1>
      <p class="identity__position">Position</p>
    </div>
    <ul class="back__contacts">
      <li class="contact">
        <svg class="contact__icon" viewBox="0 0 12 12"><path d="M6 1 L11.5 6 H10 V11 H7.3 V7.5 H4.7 V11 H2 V6 H0.5 Z"/></svg>
        <span>Av. Gervásio Tavares 418 sala 207<br>Barra da Tijuca, Rio de Janeiro, RJ Brasil</span>
      </li>
      <li class="contact">
        <svg class="contact__icon" viewBox="0 0 12 12"><path d="M2 10.5 L3.5 9 L4.2 9.7 L9.7 4.2 L9 3.5 L10.5 2 L12 3.5 L4 11.5 Z M0.5 12 L2 10.5 L2.8 11.2 Z"/></svg>
        <span>+55 21 86347215</span>
      </li>
      <li class="contact">
        <svg class="contact__icon" viewBox="0 0 12 12"><path d="M0.5 2.5 H11.5 V9.5 H0.5 Z" fill="none"/><path d="M0.5 2.5 H11.5 L6 6.5 Z M0.5 3.6 L6 7.6 L11.5 3.6 V9.5 H0.5 Z"/></svg>
        <span>osvaldo@fernloop.com.br</span>
      </li>
    </ul>
    <div class="back__brand">
      <div class="brand__figure" role="img" aria-label="Brand mascot illustration running with a briefcase and hat"></div>
      <div class="brand__name">FernLoop</div>
    </div>
  </section>
</main>
</body>
</html>
```